Business Card for a Wedding Films Business

We require a business card design for our business 'Lewis Marrow Wedding Films'. The logo needs to look classy and high end.

Target Market(s)

Wedding Couples

Contact Information for Business Card

Lewis Marrow Wedding Films
07312 605 227
films@lewismarrowreels.com
www.lewismarrowreels.com

Facebook: @lewismarrowweddingfilms
Instagram: @lewismarrowfilms

Font styles to use
Sans Serif

Requirements
Must have
• Social media icons - Facebook and Instagram

```html
<!DOCTYPE html>
<html lang="en">
<head>
<meta charset="utf-8">
<title>Lewis Marrow Wedding Films – Business Card</title>
<link rel="stylesheet" href="https://fonts.googleapis.com/css2?family=Montserrat:wght@500&family=Open+Sans:wght@600&display=swap">
<style>
  :root {
    --backdrop: #8a9099;
    --card-dark: #0c0c0d;
    --card-light: #ffffff;
    --ink-light: #f2f2f2;
    --ink-dark: #1b1b1b;
    --icon: #2a2a2a;
  }
  * { margin: 0; padding: 0; box-sizing: border-box; }
  html, body {
    width: 1200px; height: 900px; overflow: hidden;
    background: var(--backdrop);
  }
  .canvas { position: relative; width: 1200px; height: 900px; }

  .card {
    position: absolute;
    box-shadow: 0 10px 28px rgba(0,0,0,0.35);
  }

  /* Front: dark portrait card */
  .card-front {
    left: 110px; top: 250px;
    width: 340px; height: 594px;
    background: var(--card-dark);
    display: flex; align-items: flex-start; justify-content: center;
    padding-top: 150px;
  }
  .wordmark {
    font-family: "Montserrat", sans-serif;
    font-weight: 500;
    color: var(--ink-light);
    text-transform: uppercase;
    text-align: center;
    line-height: 1.5;
  }
  .wordmark .name { display: block; font-size: 27px; letter-spacing: 5px; }
  .wordmark .trade { display: block; font-size: 13px; letter-spacing: 6px; }

  /* Back: light landscape card */
  .card-back {
    left: 530px; top: 110px;
    width: 600px; height: 343px;
    background: var(--card-light);
    border: 4px solid var(--card-dark);
    display: flex; align-items: center; justify-content: space-between;
    padding: 0 44px 0 46px;
  }
  .card-back .wordmark { color: var(--ink-dark); text-align: left; margin-top: -90px; }
  .card-back .wordmark .name { font-size: 24px; letter-spacing: 4px; }
  .card-back .wordmark .trade { font-size: 12px; letter-spacing: 5px; }

  .contact-list {
    list-style: none;
    font-family: "Open Sans", sans-serif;
    font-weight: 600;
    font-size: 13.5px;
    color: var(--ink-dark);
    margin-top: 110px;
  }
  .contact-list li {
    display: flex; align-items: center; gap: 10px;
    height: 26px;
  }
  .contact-icon { width: 16px; height: 16px; flex: none; }
  .social-square {
    width: 15px; height: 15px; flex: none;
    background: var(--icon); border-radius: 2px;
  }
</style>
</head>
<body>
<main class="canvas">

  <section class="card card-front" aria-label="Business card front">
    <h1 class="wordmark">
      <span class="name">Lewis Marrow</span>
      <span class="trade">Wedding Films</span>
    </h1>
  </section>

  <section class="card card-back" aria-label="Business card back">
    <div class="wordmark">
      <span class="name">Lewis Marrow</span>
      <span class="trade">Wedding Films</span>
    </div>

    <ul class="contact-list">
      <li>
        <svg class="contact-icon" viewBox="0 0 16 16" aria-hidden="true">
          <path d="M4 1.5l2.2 3-1.3 1.6c.8 1.9 2.2 3.3 4 4l1.6-1.3 3 2.2-1.2 2.5C7 13.5 2.5 9 2 2.7z" fill="none" stroke="var(--icon)" stroke-width="1.4" stroke-linejoin="round"/>
        </svg>
        07312 605 227
      </li>
      <li>
        <svg class="contact-icon" viewBox="0 0 16 16" aria-hidden="true">
          <rect x="1.5" y="3.5" width="13" height="9" fill="none" stroke="var(--icon)" stroke-width="1.3"/>
          <path d="M1.5 3.5L8 9l6.5-5.5" fill="none" stroke="var(--icon)" stroke-width="1.3"/>
        </svg>
        films@lewismarrowreels.com
      </li>
      <li>
        <svg class="contact-icon" viewBox="0 0 16 16" aria-hidden="true">
          <circle cx="8" cy="8" r="6.3" fill="none" stroke="var(--icon)" stroke-width="1.2"/>
          <ellipse cx="8" cy="8" rx="2.8" ry="6.3" fill="none" stroke="var(--icon)" stroke-width="1.1"/>
          <path d="M1.7 8h12.6M2.8 4.8h10.4M2.8 11.2h10.4" stroke="var(--icon)" stroke-width="1.1"/>
        </svg>
        www.lewismarrowreels.com
      </li>
      <li>
        <span class="social-square" aria-hidden="true"></span>
        @lewismarrowweddingfilms
      </li>
      <li>
        <span class="social-square" aria-hidden="true"></span>
        @lewismarrowfilms
      </li>
    </ul>
  </section>

</main>
</body>
</html>
```